Better Advertisement Flyer

- On the advertisement flyer, there should be a new logo.
- As per the screenshot, the Search, Shortlist, Send, Save Buttons should be there but with a better design. The LAYOUT for the top of the flyer should be the same as the website but a change in design

Need advertisement flyer to promote directory (bridalcompass.example.sg) Uploaded is our existing flyer. REQUIRE A MUCH BETTER DESIGN

Overview of service: directory for vendors to list to their service in.
Directory will then be marketed to consumers. Main feature is the mass send
enquiry function where consumers can check off vendors and mass send their
enquiry, vendor will also receive a monthly report on how many users open
their listing. (Bridalcompass.example.sg)

Target market: for vendors to advertise in our directory

Design specifics: as per website color scheme

Contact Details to be on the flyer:
Contact Number: 6412-9076
E-mail: advertise@bridalcompass.example.sg

Please view the change in content. Also, we want to have a new look so if possible, have a new logo with the flyer. Thank you!

Target Market(s)

- Wedding Vendors for them to advertise in our directory
- Design is meant for Print Advertisement

Industry/Entity Type

It Service

Font styles to use
Serif

Colors
f9d9e8
d0ebe7
fff3d1

Requirements
Must have

• A Different Logo to Match the flyer. Logo must be Eye-Catching, different (like a magazine cover logo)

Content

Advertiser Benefits

(1) Increase Your Exposure
(2) Enquires Directed Straight To Your Inbox
(3) Featured Advertorial Post
(4) Online Reputation Management
(5) List Your Upcoming Events
(6) Advertise Your Promotions
(7) List in Multiple Categories

About The Bridal Compass

A Revolutionary online platform developed for brides who want instant contact with every Wedding Vendor in just one e-mail,

The Bridal Compass has a simple, clean and easy to use interface that lets consumers choose and mass send their enquiries!

Get potential customers in the fastest way and boost your sales revenue today!

Simple Steps To Using The Bridal Compass (Please use boxes like that of the website)
(1) Find Wedding Services using the Wedding Directory
(2) Create a list of businesses that you would like to contact
(3) Send an enquiry to multiple businesses at the same time
(4) Save Time & Money Using Wedding Deals

(Put the Email Envelope) advertise@bridalcompass.example.sg
W: bridalcompass.example.sg
Nice to have
• Color: As per the website / current colour. ( No Strong Colors) Use lesser pink and more neutral colours like green & yellow tone as per the colour palette
Open to changes but the must have colour is the green on the Website

```html
<!DOCTYPE html>
<html lang="en">
<head>
<meta charset="utf-8">
<title>The Bridal Compass – Advertise With Us</title>
<link rel="stylesheet" href="https://fonts.googleapis.com/css2?family=Playfair+Display:wght@400;700&family=Lora:ital,wght@0,400;0,500;0,600;1,400&display=swap">
<style>
  :root {
    --cream: #fff3d1;
    --mint: #d0ebe7;
    --blush: #f9d9e8;
    --green: #5f9e93;
    --green-deep: #3f7a70;
    --panel: rgba(255, 253, 246, 0.86);
    --panel-edge: rgba(95, 158, 147, 0.35);
    --ink: #4d5654;
    --ink-soft: #6f7a77;
    --white: #ffffff;
  }
  * { box-sizing: border-box; margin: 0; padding: 0; }
  html, body { width: 874px; height: 1200px; overflow: hidden; background: var(--white); }
  body { font-family: "Lora", Georgia, serif; color: var(--ink); position: relative; }

  .flyer {
    position: absolute; left: 0; top: 0; width: 874px; height: 1122px; overflow: hidden;
    background:
      radial-gradient(ellipse 360px 260px at 90px 1040px, rgba(249, 217, 232, 0.55), transparent 70%),
      radial-gradient(ellipse 420px 300px at 780px 240px, rgba(208, 235, 231, 0.9), transparent 70%),
      linear-gradient(165deg, var(--cream) 0%, #fbf6e6 45%, var(--mint) 100%);
  }

  .panel {
    position: absolute;
    background: var(--panel);
    border: 1px solid var(--panel-edge);
    border-radius: 6px;
    box-shadow: 0 3px 12px rgba(63, 122, 112, 0.15);
  }
  .panel-heading {
    font-family: "Playfair Display", Georgia, serif;
    font-weight: 700; color: var(--green-deep); line-height: 1.2;
  }

  /* Masthead */
  .masthead {
    left: 26px; top: 17px; width: 822px; height: 150px;
    border-top: 6px solid var(--green);
    display: flex; flex-direction: column; justify-content: center; padding: 0 40px;
  }
  .brand-row { display: flex; align-items: center; gap: 20px; }
  .brand-mark { width: 22px; height: 22px; border-radius: 50%; background: var(--green); flex: none; }
  .brand-name {
    font-family: "Playfair Display", Georgia, serif;
    font-weight: 700; font-size: 70px; line-height: 1; color: var(--green-deep); letter-spacing: 0.5px;
  }
  .tagline {
    margin-top: 12px; padding-left: 42px;
    font-size: 13px; font-weight: 500; letter-spacing: 2px; text-transform: uppercase; color: var(--ink-soft);
  }

  /* Steps */
  .steps { left: 26px; top: 200px; width: 458px; height: 398px; padding: 18px 21px; }
  .steps .panel-heading { font-size: 23px; margin-bottom: 18px; }
  .step-list { list-style: none; display: flex; flex-direction: column; gap: 12px; }
  .step { display: flex; align-items: center; gap: 18px; height: 58px; }
  .step-button {
    flex: none; width: 140px; height: 58px; border-radius: 12px;
    background: var(--green); color: var(--white);
    display: flex; align-items: center; justify-content: center;
    font-family: "Playfair Display", Georgia, serif; font-size: 22px; font-weight: 400;
    box-shadow: inset 0 -3px 0 var(--green-deep);
  }
  .step-text { font-size: 14px; line-height: 1.4; color: var(--ink); }

  /* Contact */
  .contact { left: 26px; top: 619px; width: 458px; height: 124px; padding: 16px 21px; background: var(--mint); }
  .contact-row { display: flex; align-items: center; gap: 12px; height: 30px; font-size: 17px; color: var(--green-deep); font-weight: 600; }
  .contact-row svg { flex: none; width: 24px; height: 24px; }
  .contact-label { font-family: "Playfair Display", Georgia, serif; width: 24px; text-align: center; font-size: 18px; }

  /* Benefits */
  .benefits { left: 507px; top: 200px; width: 341px; height: 543px; padding: 20px 22px; }
  .benefits .panel-heading { font-size: 27px; margin-bottom: 16px; }
  .benefit-list { list-style: none; display: flex; flex-direction: column; gap: 13px; }
  .benefit { display: flex; align-items: flex-start; gap: 12px; font-size: 17px; line-height: 1.35; }
  .benefit-number {
    flex: none; width: 30px; height: 30px; border-radius: 50%;
    background: var(--cream); border: 2px solid var(--green);
    color: var(--green-deep); font-weight: 600; font-size: 15px;
    display: flex; align-items: center; justify-content: center; margin-top: -3px;
  }

  /* About */
  .about { left: 26px; top: 775px; width: 822px; height: 284px; padding: 20px 30px; border-left: 6px solid var(--blush); }
  .about .panel-heading { font-size: 26px; margin-bottom: 10px; }
  .about p { font-size: 17.5px; line-height: 1.55; color: var(--ink); margin-bottom: 10px; }
  .about .call-to-action { font-weight: 600; color: var(--green-deep); margin-bottom: 0; }

  .site-url {
    position: absolute; left: 0; width: 874px; top: 1078px;
    text-align: center; font-family: "Playfair Display", Georgia, serif; font-size: 19px; color: var(--green-deep);
  }

  .contact-footer {
    position: absolute; left: 0; top: 1122px; width: 874px; height: 78px;
    display: flex; align-items: center; justify-content: center; gap: 34px;
    font-size: 15px; font-style: italic; color: var(--ink-soft);
    border-top: 4px solid var(--green);
  }
</style>
</head>
<body>
  <main class="flyer">
    <header class="panel masthead">
      <div class="brand-row">
        <span class="brand-mark"></span>
        <h1 class="brand-name">The Bridal Compass</h1>
      </div>
      <p class="tagline">The fastest way to find wedding services in Singapore</p>
    </header>

    <section class="panel steps">
      <h2 class="panel-heading">Simple Steps To Using<br>The Bridal Compass</h2>
      <ol class="step-list">
        <li class="step"><span class="step-button">Search</span><p class="step-text">Find Wedding Services using the Wedding Directory</p></li>
        <li class="step"><span class="step-button">Shortlist</span><p class="step-text">Create a list of businesses that you would like to contact</p></li>
        <li class="step"><span class="step-button">Send</span><p class="step-text">Send an enquiry to multiple businesses at the same time</p></li>
        <li class="step"><span class="step-button">Save</span><p class="step-text">Save Time &amp; Money Using Wedding Deals</p></li>
      </ol>
    </section>

    <aside class="panel contact">
      <p class="contact-row">
        <svg viewBox="0 0 24 24" aria-hidden="true"><rect x="2" y="5" width="20" height="14" rx="2" fill="none" stroke="#3f7a70" stroke-width="2"/><path d="M2.5 6 L12 13 L21.5 6" fill="none" stroke="#3f7a70" stroke-width="2"/></svg>
        advertise@bridalcompass.example.sg
      </p>
      <p class="contact-row">
        <svg viewBox="0 0 24 24" aria-hidden="true"><path d="M6.6 10.8a15 15 0 0 0 6.6 6.6l2.2-2.2a1 1 0 0 1 1-.25 11.4 11.4 0 0 0 3.6.6 1 1 0 0 1 1 1V20a1 1 0 0 1-1 1A17 17 0 0 1 3 4a1 1 0 0 1 1-1h3.5a1 1 0 0 1 1 1c0 1.25.2 2.45.6 3.6a1 1 0 0 1-.25 1z" fill="#3f7a70"/></svg>
        6412-9076
      </p>
      <p class="contact-row"><span class="contact-label">W:</span> bridalcompass.example.sg</p>
    </aside>

    <section class="panel benefits">
      <h2 class="panel-heading">Advertiser Benefits</h2>
      <ol class="benefit-list">
        <li class="benefit"><span class="benefit-number">1</span>Increase Your Exposure</li>
        <li class="benefit"><span class="benefit-number">2</span>Enquires Directed Straight To Your Inbox</li>
        <li class="benefit"><span class="benefit-number">3</span>Featured Advertorial Post</li>
        <li class="benefit"><span class="benefit-number">4</span>Online Reputation Management</li>
        <li class="benefit"><span class="benefit-number">5</span>List Your Upcoming Events</li>
        <li class="benefit"><span class="benefit-number">6</span>Advertise Your Promotions</li>
        <li class="benefit"><span class="benefit-number">7</span>List in Multiple Categories</li>
      </ol>
    </section>

    <section class="panel about">
      <h2 class="panel-heading">About The Bridal Compass</h2>
      <p>A Revolutionary online platform developed for brides who want instant contact with every Wedding Vendor in just one e-mail.</p>
      <p>The Bridal Compass has a simple, clean and easy to use interface that lets consumers choose and mass send their enquiries!</p>
      <p class="call-to-action">Get potential customers in the fastest way and boost your sales revenue today!</p>
    </section>

    <p class="site-url">bridalcompass.example.sg</p>
  </main>

  <footer class="contact-footer">
    <span>T: 6412-9076</span>
    <span>E: advertise@bridalcompass.example.sg</span>
    <span>W: bridalcompass.example.sg</span>
  </footer>
</body>
</html>
```